Create Lanternfield HR Business Cards.

Create Business Cards for Lanternfield HR. 2 sided and Would like the back to have the logo.

Info for Business Card:
Address: 4827 Millbrook Ave Suite 230 Cleveland, Ohio 44987
Office Number: 216-555-0143
Mobile: 216-555-0192

Website: www.lanternfieldhr.example

Target Market(s)

Small to medium size businesses

Industry/Entity Type

Human Resources

Contact Information for Business Card

Company logo and information

Font styles to use
Serif
Sans Serif

Requirements
Must have
• Info for Business Card: Address: 4827 Millbrook Ave Suite 230 Cleveland, Ohio 44987 Office Number: 216-555-0143 Mobile: 216-555-0192 Website: www.lanternfieldhr.example

```html
<!DOCTYPE html>
<html lang="en">
<head>
<meta charset="utf-8">
<title>Lanternfield HR Business Cards</title>
<link rel="stylesheet" href="https://fonts.googleapis.com/css2?family=Montserrat:wght@700&family=Poppins:wght@400;600&display=swap">
<style>
  :root{
    --stage:#cccccc;
    --navy:#0e3179;
    --indigo:#27215e;
    --orange:#ff8500;
    --orange-soft:#f47b30;
    --teal:#118bb3;
    --white:#ffffff;
  }
  *{margin:0;padding:0;box-sizing:border-box}
  html,body{width:1200px;height:1200px;overflow:hidden}
  body{background:var(--stage);position:relative;font-family:"Poppins",sans-serif}
  .card{position:absolute;left:207px;width:787px;height:471px;overflow:hidden}
  .card--front{top:119px;background:var(--navy);color:var(--white)}
  .card--back{top:614px;background:var(--white)}

  .texture{position:absolute}
  .card--front .texture{background:linear-gradient(180deg,rgba(255,255,255,.05),rgba(255,255,255,.02))}
  .card--back .texture{background:linear-gradient(180deg,rgba(39,33,94,.07),rgba(39,33,94,.03))}
  .texture--right-a{left:602px;top:0;width:48px;height:148px}
  .texture--right-b{left:658px;top:0;width:48px;height:225px}
  .texture--right-c{left:714px;top:0;width:47px;height:302px}
  .texture--left-a{left:25px;top:248px;width:48px;height:223px}
  .texture--left-b{left:81px;top:326px;width:48px;height:145px}
  .texture--left-c{left:137px;top:404px;width:47px;height:67px}

  .top-band{position:absolute;left:25px;top:22px;width:338px;height:35px;border-radius:0 0 36px 0;overflow:hidden}
  .top-band::before{content:"";position:absolute;inset:0 0 auto 0;height:6px;background:var(--orange)}
  .card--front .top-band{background:var(--indigo)}
  .card--back .top-band{background:var(--teal)}
  .card--back .top-band::before{background:var(--orange-soft)}

  .divider{position:absolute;left:394px;top:52px;width:1px;height:379px;background:rgba(255,255,255,.12)}

  .person-name{position:absolute;left:67px;top:91px;font-family:"Montserrat",sans-serif;font-weight:700;font-size:38px;letter-spacing:1.5px;line-height:1}
  .person-role{position:absolute;left:67px;top:131px;font-size:20px;line-height:1}

  .contact{position:absolute;left:67px;top:246px;list-style:none}
  .contact li{display:flex;align-items:flex-start;font-size:20.5px;line-height:29px;letter-spacing:.5px;margin-bottom:6px}
  .contact svg{width:22px;height:22px;flex:none;margin:3px 13px 0 0}

  .brand{position:absolute;display:flex;align-items:center;gap:12px;font-weight:600;font-size:30px;line-height:1;white-space:nowrap}
  .brand__dot{width:26px;height:26px;border-radius:50%;flex:none}
  .card--front .brand{left:460px;top:200px;color:var(--white)}
  .card--front .brand__dot{background:var(--white)}
  .card--back .brand{left:273px;top:222px;color:var(--indigo)}
  .card--back .brand__dot{background:var(--orange)}

  .web-band{position:absolute;left:394px;top:402px;width:367px;height:41px;background:var(--indigo);border-radius:36px 0 0 0;overflow:hidden}
  .web-band::after{content:"";position:absolute;left:0;right:0;bottom:0;height:6px;background:var(--orange-soft)}
  .web-band span{position:absolute;left:0;right:0;top:8px;text-align:center;font-size:17px;letter-spacing:.4px}

  .base-line{position:absolute;left:32px;top:434px;width:729px;height:12px;border-radius:8px 8px 0 0;background:var(--indigo);overflow:hidden}
  .base-line::after{content:"";position:absolute;left:0;right:0;bottom:0;height:6px;background:var(--orange-soft);border-radius:6px 6px 0 0}
</style>
</head>
<body>

<section class="card card--front" aria-label="Business card front">
  <div class="texture texture--right-a" role="img" aria-label="Faint chevron stripe pattern"></div>
  <div class="texture texture--right-b" role="img" aria-label="Faint chevron stripe pattern"></div>
  <div class="texture texture--right-c" role="img" aria-label="Faint chevron stripe pattern"></div>
  <div class="texture texture--left-a" role="img" aria-label="Faint chevron stripe pattern"></div>
  <div class="texture texture--left-b" role="img" aria-label="Faint chevron stripe pattern"></div>
  <div class="texture texture--left-c" role="img" aria-label="Faint chevron stripe pattern"></div>

  <div class="top-band"></div>
  <div class="divider"></div>

  <h1 class="person-name">PERSON NAME</h1>
  <p class="person-role">HR Head</p>

  <ul class="contact">
    <li>
      <svg viewBox="0 0 24 24" fill="none" stroke="#fff" stroke-width="1.3" stroke-linecap="round" stroke-linejoin="round"><path d="M5 3.5l3 .2 1.6 4-2 1.4a11 11 0 0 0 6.3 6.3l1.4-2 4 1.6.2 3c0 1-1 2-2 2A16.5 16.5 0 0 1 3 5.5c0-1 1-2 2-2z"/><path d="M14 3.5a6.5 6.5 0 0 1 6.5 6.5M14 6.5a3.5 3.5 0 0 1 3.5 3.5"/></svg>
      <span>216-555-0143 (Office)</span>
    </li>
    <li>
      <svg viewBox="0 0 24 24" fill="none" stroke="#fff" stroke-width="1.3" stroke-linejoin="round"><rect x="2.5" y="5" width="19" height="14" rx="1.5"/><path d="M2.5 6l9.5 7.5L21.5 6M2.5 18.5l7-6.5M21.5 18.5l-7-6.5"/></svg>
      <span>216-555-0192</span>
    </li>
    <li>
      <svg viewBox="0 0 24 24" fill="none" stroke="#fff" stroke-width="1.3"><path d="M12 22s-7-6.8-7-12.5a7 7 0 0 1 14 0C19 15.2 12 22 12 22z"/><circle cx="12" cy="9.5" r="3.5"/></svg>
      <span>4827 Millbrook Ave Suite<br>230 Cleveland, Ohio 44987</span>
    </li>
  </ul>

  <div class="brand"><span class="brand__dot"></span>Lanternfield HR</div>

  <div class="web-band"><span>www.lanternfieldhr.example</span></div>
</section>

<section class="card card--back" aria-label="Business card back">
  <div class="texture texture--right-a" role="img" aria-label="Faint chevron stripe pattern"></div>
  <div class="texture texture--right-b" role="img" aria-label="Faint chevron stripe pattern"></div>
  <div class="texture texture--right-c" role="img" aria-label="Faint chevron stripe pattern"></div>
  <div class="texture texture--left-a" role="img" aria-label="Faint chevron stripe pattern"></div>
  <div class="texture texture--left-b" role="img" aria-label="Faint chevron stripe pattern"></div>
  <div class="texture texture--left-c" role="img" aria-label="Faint chevron stripe pattern"></div>

  <div class="top-band"></div>

  <div class="brand"><span class="brand__dot"></span>Lanternfield HR</div>

  <div class="base-line"></div>
</section>

</body>
</html>
```